Nail salon window signage design

We need new signage to be designed for our existing nail salon. The sign will be a large sticker that will stick onto the glass window at the front.

Some of the services we provide are:
Manicures
Pedicures
Velora Gel Builder
Acrylic Nails
KVT
Brenlux
Gel Polish
You may wish to have our services listed on the sign but is not compulsory.

I have also attached our logo which can be used on the sign but is not compulsory.

I have also attached a photo of the front of our salon and the sign will be where I have outlined in yellow.

The size of the sign will be 119cm wide and 170cm high.

I am open to any nice classy design you can think of.

```html
<!DOCTYPE html>
<html lang="en">
<head>
<meta charset="utf-8">
<title>Amberly Nails – Services List</title>
<link rel="stylesheet" href="https://fonts.googleapis.com/css2?family=Playfair+Display:ital,wght@1,900&family=Sorts+Mill+Goudy&display=swap">
<style>
  :root {
    --paper: #fdf7f9;
    --blush: #f3d9e2;
    --blush-soft: #f8e8ee;
    --wine: #8e1e33;
    --navy: #1f1850;
  }
  html, body {
    margin: 0;
    padding: 0;
    overflow: hidden;
    background: var(--paper);
  }
  .sign {
    position: relative;
    width: 840px;
    height: 1200px;
    overflow: hidden;
    background:
      radial-gradient(ellipse 260px 420px at 0% 30%, var(--blush) 0%, transparent 70%),
      radial-gradient(ellipse 300px 380px at 100% 88%, var(--blush) 0%, transparent 70%),
      radial-gradient(ellipse 260px 200px at 40% 100%, var(--blush-soft) 0%, transparent 70%),
      var(--paper);
  }
  .brand-name {
    position: absolute;
    top: 170px;
    left: 0;
    width: 840px;
    margin: 0;
    text-align: center;
    font-family: "Sorts Mill Goudy", serif;
    font-weight: 400;
    font-size: 104px;
    line-height: 1;
    color: var(--wine);
  }
  .services-title {
    position: absolute;
    top: 362px;
    left: 0;
    width: 840px;
    margin: 0;
    text-align: center;
    font-family: "Playfair Display", serif;
    font-style: italic;
    font-weight: 900;
    font-size: 80px;
    line-height: 1;
    color: var(--navy);
  }
  .services {
    position: absolute;
    top: 466px;
    left: 0;
    width: 840px;
    margin: 0;
    padding: 0;
    list-style: none;
    text-align: center;
    font-family: "Sorts Mill Goudy", serif;
    font-size: 42px;
    line-height: 68.5px;
    color: var(--navy);
  }
  .ornament {
    position: absolute;
    top: 945px;
    left: 92px;
    width: 656px;
    height: 180px;
    border-radius: 50% 50% 50% 50% / 40% 40% 60% 60%;
    background: radial-gradient(ellipse at 50% 55%, rgba(142,30,51,0.55) 0%, rgba(142,30,51,0.18) 55%, rgba(142,30,51,0) 75%);
  }
</style>
</head>
<body>
  <main class="sign">
    <h1 class="brand-name">Amberly Nails</h1>
    <h2 class="services-title">services list</h2>
    <ul class="services">
      <li>Velora Gel Builder</li>
      <li>Acrylic Nails</li>
      <li>Manicures</li>
      <li>Gel Polish</li>
      <li>Pedicures</li>
      <li>Brenlux</li>
      <li>KVT</li>
    </ul>
    <div class="ornament" role="img" aria-label="Wine-red decorative flourish with swirls and scattered dots"></div>
  </main>
</body>
</html>
```